Redesign responsive website and logo for webshop platform

Redesign our applications old website with a new clean, crisp modern looking style that is responsive.

Our application is a cloud based, free ecommerce platform that lets users set up their own webshops within minutes. (Similar to Bramvik https://bramvik.example/l/sell)

Our old website: http://sv.kelporia.example/

I need redesigned HTML + CSS for the following three pages:
* Landing Page:
(Old page: http://sv.kelporia.example/)
I have attached a mockup of a proposed layout/structure for the landing page.
- Pricing comparision/features page
(Old page http://sv.kelporia.example/t/funktioner)
- Generic "article" page:
(Old page http://sv.kelporia.example/d/redigerasida)

The pages must responsive using HTML 5/CSS 3 (I prefer Bootstrap 3 if possible).

I also need a redesign of the logotype.

If you have any questions don't hesitate to ask and we will provide whatever is needed to you.

Logo Text

Kelporia

Coding

Coded - Design and coding required

Number of Pages Required

3 page

Font styles to use
Serif
Sans Serif

```html
<!DOCTYPE html>
<html lang="sv">
<head>
<meta charset="utf-8">
<title>Kelporia – Starta en gratis webshop</title>
<link rel="stylesheet" href="https://fonts.googleapis.com/css2?family=Roboto:wght@300;400;500&display=swap">
<style>
:root{
  --blue:#3f97d8;
  --blue-light:#d8eaf8;
  --navy:#141b2b;
  --navy-2:#1c2438;
  --page:#f2f2f2;
  --card:#ffffff;
  --text:#333a44;
  --muted:#7a808a;
  --line:#d9dde2;
  --white:#ffffff;
}
*{box-sizing:border-box;margin:0;padding:0}
html,body{width:1200px;height:900px;overflow:hidden}
body{font-family:"Roboto",Arial,sans-serif;color:var(--text);background:var(--white);font-size:12px}
.wrap{width:960px;margin:0 auto;position:relative}

/* header */
.site-header{height:52px;background:var(--white);border-bottom:1px solid #e6e6e6}
.site-header .wrap{display:flex;align-items:center;justify-content:space-between;height:52px}
.brand{font-size:26px;font-weight:400;color:var(--blue);letter-spacing:.3px}
.login{font-size:13px;color:var(--muted);display:flex;align-items:center;gap:6px}

/* hero */
.hero{height:180px;position:relative;overflow:hidden;color:var(--white);text-align:center}
.hero-bg{position:absolute;inset:0;background:linear-gradient(180deg,#1d2740 0%,#121829 100%)}
.hero .wrap{padding-top:30px}
.hero h1{font-weight:300;font-size:34px;color:#a9d3f5;margin-bottom:10px}
.hero p{font-size:13px;margin-bottom:26px}
.signup{display:flex;justify-content:center;gap:4px}
.signup .field{width:210px;height:34px;background:var(--white);color:#8a8f96;font-size:12px;text-align:left;padding:10px 10px}
.signup .btn{height:34px;padding:0 18px;background:var(--blue);color:var(--white);font-size:12px;display:flex;align-items:center}

/* features */
.features{background:var(--page);height:240px;padding-top:16px}
.feature-grid{display:grid;grid-template-columns:1fr 1fr;gap:12px 20px}
.feature{background:var(--card);height:62px;display:flex;align-items:center;gap:16px;padding:0 20px}
.feature svg{flex:none}
.feature h3{font-weight:400;font-size:14px;color:#555c66;margin-bottom:4px}
.feature p{font-size:10.5px;color:var(--muted);line-height:1.35}

/* small features */
.small-features{background:var(--navy);height:110px;padding-top:14px}
.small-grid{display:grid;grid-template-columns:repeat(3,1fr);gap:10px 18px}
.small-item{border:1px solid #59627a;height:38px;text-align:center;padding-top:6px}
.small-item h4{font-weight:400;font-size:12px;color:#aeb6c6;margin-bottom:3px}
.small-item p{font-size:10px;color:#e6e9ef}

/* pricing */
.pricing{height:210px;padding-top:10px;text-align:center}
.pricing h2{font-weight:400;font-size:14px;color:#6a7079;letter-spacing:.5px;margin-bottom:8px}
.price-table{display:grid;grid-template-columns:480px 220px 220px;gap:0 20px;text-align:center}
.col{border:1px solid var(--line);background:#f7f7f7}
.col .head{height:24px;line-height:24px;font-size:12px;font-weight:500}
.col .row{height:15px;line-height:15px;font-size:10.5px;border-bottom:1px solid #e3e5e8;margin:0 6px}
.col .foot{height:22px;line-height:22px;font-size:12px;font-weight:500;margin-top:4px}
.col.features-col .head{background:#f7f7f7}
.col.features-col .row{background:var(--white)}
.col.basic .row{background:var(--white)}
.col.premium{background:var(--blue-light);border-color:var(--blue)}
.col.premium .head{background:var(--blue);color:var(--white);font-weight:400}
.col.premium .row{border-bottom-color:#a9cdec}
.col.premium .foot{background:var(--blue);color:var(--white)}
.tick{display:inline-block;vertical-align:middle}
.more{display:inline-block;margin-top:7px;padding:5px 14px;border:1px solid var(--line);font-size:11px;color:var(--text)}

/* call to action */
.cta{height:68px;position:relative;background:var(--navy);text-align:center;color:var(--white)}
.cta-bg{position:absolute;inset:0;background:linear-gradient(180deg,#1b2439,#121828)}
.cta .wrap{padding-top:6px}
.cta h2{font-weight:300;font-size:24px;color:#a9d3f5;margin-bottom:6px}
.cta .signup .field,.cta .signup .btn{height:22px;padding-top:0;padding-bottom:0;display:flex;align-items:center}

/* footer */
.site-footer{height:40px}
.site-footer .wrap{display:flex;justify-content:space-between;align-items:center;height:40px}
.legal{font-size:10.5px;color:var(--blue)}
.legal span{color:var(--muted)}
.social{display:flex;gap:12px;align-items:center}
</style>
</head>
<body>

<header class="site-header">
  <div class="wrap">
    <div class="brand">Kelporia</div>
    <div class="login">
      <svg width="13" height="13" viewBox="0 0 14 14" fill="none" stroke="#7a808a" stroke-width="1.5"><path d="M6 2h6v10H6"/><path d="M1 7h7M5.5 4.5 8 7l-2.5 2.5"/></svg>
      Logga in
    </div>
  </div>
</header>

<section class="hero">
  <div class="hero-bg" role="img" aria-label="Dämpad bakgrundsbild med skärmbilder av webbutiker"></div>
  <div class="wrap">
    <h1>Starta en gratis webshop</h1>
    <p>Tjänsten är gratis och har allt som krävs för att du ska komma igång med din verksamhet och sälja produkter online</p>
    <div class="signup"><div class="field">Namnet på din butik</div><div class="btn">Skapa en webshop</div></div>
  </div>
</section>

<section class="features">
  <div class="wrap feature-grid">
    <div class="feature">
      <svg width="34" height="34" viewBox="0 0 34 34" fill="none" stroke="#3f97d8" stroke-width="3"><circle cx="17" cy="17" r="14"/><path d="M17 9v9h7"/></svg>
      <div><h3>Kom igång på 5 minuter</h3><p>Allt startas en ebutik med Kelporia tar inte mer än 5 minuter. Skapa ett konto för att komma igång. Ingenting behöver installeras på din dator</p></div>
    </div>
    <div class="feature">
      <svg width="34" height="34" viewBox="0 0 34 34"><text x="17" y="29" text-anchor="middle" font-family="Roboto,Arial,sans-serif" font-size="34" font-weight="500" fill="#3f97d8">$</text></svg>
      <div><h3>Skapa en gratis webbutik</h3><p>Kelporia är en gratis tjänst. Tjänsten har varken månadskostnader eller transaktionsavgifter på din sidan</p></div>
    </div>
    <div class="feature">
      <svg width="34" height="34" viewBox="0 0 34 34" fill="#3f97d8"><rect x="2" y="4" width="30" height="7" rx="1"/><rect x="2" y="13.5" width="30" height="7" rx="1"/><rect x="2" y="23" width="30" height="7" rx="1"/></svg>
      <div><h3>Intuitivt användargränssnitt</h3><p>Det går snabbt att lägga till nya produkter. Organisera produkter genom att dra och släppa</p></div>
    </div>
    <div class="feature">
      <svg width="34" height="34" viewBox="0 0 34 34" fill="#3f97d8"><rect x="3" y="18" width="7" height="14"/><rect x="13" y="6" width="7" height="26"/><rect x="23" y="13" width="7" height="19"/></svg>
      <div><h3>Sökmotoroptimerad</h3><p>Kelporia är genomgående skapat med sökmotoroptimering som en fokuspunkt</p></div>
    </div>
    <div class="feature">
      <svg width="34" height="34" viewBox="0 0 34 34" fill="none" stroke="#3f97d8" stroke-width="3"><path d="M16 5H5v24h24V18"/><path d="M13 21l2-6 12-12 4 4-12 12z"/></svg>
      <div><h3>Designa din webshop</h3><p>Välj bland färdiga utseendemallar eller skapa din egen grafiska profil med ett par klick</p></div>
    </div>
    <div class="feature">
      <svg width="34" height="34" viewBox="0 0 34 34" fill="#3f97d8"><rect x="2" y="5" width="5" height="4"/><rect x="10" y="5" width="22" height="4"/><rect x="2" y="12" width="5" height="4"/><rect x="10" y="12" width="22" height="4"/><rect x="2" y="19" width="5" height="4"/><rect x="10" y="19" width="22" height="4"/><rect x="2" y="26" width="5" height="4"/><rect x="10" y="26" width="22" height="4"/></svg>
      <div><h3>Smart Dashboard</h3><p>Få överblick i din webbutik så du får koll på senast inkomna order, analys och statistik om försäljningar mm.</p></div>
    </div>
  </div>
</section>

<section class="small-features">
  <div class="wrap small-grid">
    <div class="small-item"><h4>Small feature 1</h4><p>Lorem ipsum dolor sit amet consectetuer</p></div>
    <div class="small-item"><h4>Small feature 2</h4><p>Lorem ipsum dolor sit amet consectetuer</p></div>
    <div class="small-item"><h4>Small feature 3</h4><p>Lorem ipsum dolor sit amet consectetuer</p></div>
    <div class="small-item"><h4>Small feature 5</h4><p>Lorem ipsum dolor sit amet consectetuer</p></div>
    <div class="small-item"><h4>Small feature 5</h4><p>Lorem ipsum dolor sit amet consectetuer</p></div>
    <div class="small-item"><h4>Small feature 6</h4><p>Lorem ipsum dolor sit amet consectetuer</p></div>
  </div>
</section>

<section class="pricing">
  <div class="wrap">
    <h2>FUNKTIONER</h2>
    <div class="price-table">
      <div class="col features-col">
        <div class="head"></div>
        <div class="row">0 Transaktionsavgift</div>
        <div class="row">Obegränsat antal produkter</div>
        <div class="row">Lagerhantering</div>
        <div class="row">Rabattkoder</div>
        <div class="row">Egen domän</div>
        <div class="row">Searvo Ads kupong (värde 750kr)</div>
        <div class="foot"></div>
      </div>
      <div class="col basic">
        <div class="head">Basic</div>
        <div class="row"><svg class="tick" width="10" height="10" viewBox="0 0 10 10" fill="none" stroke="#555" stroke-width="1.4"><circle cx="5" cy="5" r="4"/><path d="M3 5l1.5 1.5L8 3"/></svg></div>
        <div class="row"><svg class="tick" width="10" height="10" viewBox="0 0 10 10" fill="none" stroke="#555" stroke-width="1.4"><circle cx="5" cy="5" r="4"/><path d="M3 5l1.5 1.5L8 3"/></svg></div>
        <div class="row"><svg class="tick" width="10" height="10" viewBox="0 0 10 10" fill="none" stroke="#555" stroke-width="1.4"><circle cx="5" cy="5" r="4"/><path d="M3 5l1.5 1.5L8 3"/></svg></div>
        <div class="row"></div>
        <div class="row"></div>
        <div class="row"></div>
        <div class="foot">FREE</div>
      </div>
      <div class="col premium">
        <div class="head">Premium</div>
        <div class="row"><svg class="tick" width="10" height="10" viewBox="0 0 10 10" fill="none" stroke="#555" stroke-width="1.4"><circle cx="5" cy="5" r="4"/><path d="M3 5l1.5 1.5L8 3"/></svg></div>
        <div class="row"><svg class="tick" width="10" height="10" viewBox="0 0 10 10" fill="none" stroke="#555" stroke-width="1.4"><circle cx="5" cy="5" r="4"/><path d="M3 5l1.5 1.5L8 3"/></svg></div>
        <div class="row"><svg class="tick" width="10" height="10" viewBox="0 0 10 10" fill="none" stroke="#555" stroke-width="1.4"><circle cx="5" cy="5" r="4"/><path d="M3 5l1.5 1.5L8 3"/></svg></div>
        <div class="row"><svg class="tick" width="10" height="10" viewBox="0 0 10 10" fill="none" stroke="#555" stroke-width="1.4"><circle cx="5" cy="5" r="4"/><path d="M3 5l1.5 1.5L8 3"/></svg></div>
        <div class="row"><svg class="tick" width="10" height="10" viewBox="0 0 10 10" fill="none" stroke="#555" stroke-width="1.4"><circle cx="5" cy="5" r="4"/><path d="M3 5l1.5 1.5L8 3"/></svg></div>
        <div class="row"><svg class="tick" width="10" height="10" viewBox="0 0 10 10" fill="none" stroke="#555" stroke-width="1.4"><circle cx="5" cy="5" r="4"/><path d="M3 5l1.5 1.5L8 3"/></svg></div>
        <div class="foot">149kr /mån</div>
      </div>
    </div>
    <div class="more">Visa fler funktioner</div>
  </div>
</section>

<section class="cta">
  <div class="cta-bg" role="img" aria-label="Dämpad bakgrundsbild med skärmbilder av webbutiker"></div>
  <div class="wrap">
    <h2>Starta en gratis webshop</h2>
    <div class="signup"><div class="field">dinbutik.kelporia.example</div><div class="btn">Skapa en webshop</div></div>
  </div>
</section>

<footer class="site-footer">
  <div class="wrap">
    <div class="legal"><span>© 2016 Norvale |</span> Support <span>|</span> Dokumentation</div>
    <div class="social">
      <svg width="20" height="14" viewBox="0 0 20 14" fill="none" stroke="#b9bec5" stroke-width="1.6"><rect x="1" y="1" width="18" height="12"/><path d="M1 1l9 7 9-7M1 13l6-6M19 13l-6-6"/></svg>
      <svg width="16" height="16" viewBox="0 0 16 16"><circle cx="8" cy="8" r="7" fill="#b9bec5"/></svg>
    </div>
  </div>
</footer>

</body>
</html>
```